Book Cover for Productivity Book

I need a book cover for my latest publication "On Momentum: The Gathered Insights of the Most Tireless Woman Living"

You can see my branding at www.brightvarno.com

This is meant to be my epic pinaccle work on productivity, I want it to look like the end all be all word on productivity.

Target Market(s)

entrepreneurs

```html
<!DOCTYPE html>
<html lang="en">
<head>
<meta charset="utf-8">
<title>On Momentum – Book Cover</title>
<link rel="stylesheet" href="https://fonts.googleapis.com/css2?family=Stint+Ultra+Condensed&display=swap">
<style>
  :root {
    --cover-black: #050505;
    --suit-dark: #0d0d0f;
    --shirt-grey: #3c3f44;
    --title-red: #c9242c;
    --title-white: #ffffff;
  }
  html, body {
    margin: 0;
    padding: 0;
    width: 941px;
    height: 1200px;
    overflow: hidden;
    background: var(--cover-black);
  }
  .cover {
    position: relative;
    width: 941px;
    height: 1200px;
    overflow: hidden;
    background: var(--cover-black);
    font-family: "Stint Ultra Condensed", "Times New Roman", serif;
    text-align: center;
  }
  .cover-photo {
    position: absolute;
    inset: 0;
    background:
      radial-gradient(ellipse 22% 48% at 56% 34%, rgba(74,78,84,0.55), rgba(60,63,68,0.15) 70%, transparent 100%),
      radial-gradient(ellipse 55% 45% at 50% 45%, rgba(24,24,27,0.9), transparent 80%),
      linear-gradient(180deg, var(--suit-dark) 0%, #111114 45%, var(--cover-black) 85%);
  }
  .title-lead {
    position: absolute;
    top: 28px;
    left: 0;
    right: 0;
    margin: 0;
    font-size: 230px;
    line-height: 1;
    font-weight: 400;
    color: var(--title-white);
    letter-spacing: 2px;
  }
  .title-main {
    position: absolute;
    top: 205px;
    left: 0;
    right: 0;
    margin: 0;
    font-size: 270px;
    line-height: 1;
    font-weight: 400;
    color: var(--title-red);
    letter-spacing: 1px;
  }
  .subtitle {
    position: absolute;
    top: 730px;
    left: 0;
    right: 0;
    margin: 0;
    font-size: 78px;
    line-height: 116px;
    font-weight: 400;
  }
  .subtitle span { display: block; }
  .subtitle .sub-red { color: var(--title-red); }
  .subtitle .sub-white { color: var(--title-white); }
  .brand-name {
    position: absolute;
    right: 22px;
    bottom: 28px;
    margin: 0;
    font-size: 40px;
    line-height: 1;
    color: var(--title-red);
  }
</style>
</head>
<body>
  <main class="cover">
    <div class="cover-photo" role="img" aria-label="Dark photograph of a man in a black suit and white shirt adjusting his jacket"></div>
    <h1 class="title-lead">ON</h1>
    <p class="title-main">Momentum</p>
    <h2 class="subtitle">
      <span class="sub-red">The Gathered Insights</span>
      <span class="sub-red">of the</span>
      <span class="sub-white">Most Tireless Woman Living</span>
    </h2>
    <p class="brand-name">Bright Varno</p>
  </main>
</body>
</html>
```